Surviving Domestic Violence Flyer

I need a flyer that "POPS" to attract participants for my research project. I have added the important information on my draft flyer.

```html
<!DOCTYPE html>
<html lang="en">
<head>
<meta charset="utf-8">
<title>Survivor Research Study Flyer</title>
<link href="https://fonts.googleapis.com/css2?family=Oswald:wght@600;700&family=Montserrat:wght@300;400;600;700&display=swap" rel="stylesheet">
<style>
  :root {
    --page-bg: #ececec;
    --magenta: #ff10d8;
    --magenta-light: #ff6ee6;
    --headline: #ff22e6;
    --panel: rgba(120, 60, 120, 0.55);
    --title-band: rgba(110, 60, 90, 0.7);
    --white: #ffffff;
    --photo-dark: #1a1612;
    --photo-olive: #5b5a3a;
  }
  * { box-sizing: border-box; margin: 0; padding: 0; }
  html, body { width: 874px; height: 1200px; overflow: hidden; }
  body { background: var(--page-bg); font-family: "Montserrat", Arial, sans-serif; }

  .flyer {
    position: absolute; left: 17px; top: 55px;
    width: 840px; height: 1090px;
    background: var(--magenta);
  }

  .hero { position: relative; height: 604px; overflow: hidden; }
  .hero-photo {
    position: absolute; inset: 0;
    background:
      radial-gradient(ellipse at 82% 22%, #6f6e48 0%, rgba(90,88,58,0.7) 22%, transparent 48%),
      radial-gradient(ellipse at 72% 70%, rgba(120,80,90,0.6) 0%, transparent 40%),
      radial-gradient(ellipse at 40% 45%, #3d3724 0%, transparent 55%),
      linear-gradient(180deg, var(--photo-dark) 0%, #2a2419 45%, #1e1a14 100%);
  }
  .title-band {
    position: absolute; left: 0; top: 26px;
    width: 545px; height: 69px;
    background: var(--title-band);
    display: flex; align-items: center; padding-left: 32px;
  }
  .title-band h1 {
    font-family: "Oswald", Impact, sans-serif; font-weight: 700;
    color: var(--white); font-size: 36px; letter-spacing: 0.2px;
  }
  .headline {
    position: absolute; left: 32px; top: 126px;
    font-family: "Oswald", Impact, sans-serif; font-weight: 700;
    color: var(--headline); font-size: 44px; line-height: 54px;
  }
  .questions {
    position: absolute; left: 0; top: 317px;
    width: 739px; height: 280px;
    background: var(--panel);
    padding: 12px 0 0 42px;
    list-style: none;
  }
  .questions li {
    color: var(--white); font-weight: 700; font-size: 19.5px;
    line-height: 46px; padding-left: 16px; text-indent: -16px;
  }
  .questions li::before { content: "• "; }

  .details {
    height: 274px; padding: 44px 32px 0 26px;
    color: var(--white); font-weight: 300; font-size: 15.5px; line-height: 19px;
  }
  .details p { margin-bottom: 10px; }
  .details strong { font-weight: 700; }

  .strip { height: 16px; background: var(--magenta-light); }

  .tear-offs { display: flex; height: 196px; }
  .tab {
    flex: 1; border-right: 1px dashed rgba(255,255,255,0.55);
    display: flex; align-items: center; justify-content: center;
  }
  .tab:last-child { border-right: none; }
  .tab span {
    writing-mode: vertical-rl; transform: rotate(180deg);
    color: var(--white); font-size: 14px; line-height: 17px;
    text-align: center; white-space: nowrap;
  }
  .tab .tab-phone { font-weight: 700; font-size: 15px; }
</style>
</head>
<body>
  <main class="flyer">
    <section class="hero">
      <div class="hero-photo" role="img" aria-label="Dim photograph of a hooded person in an olive jacket sitting with clasped hands, face hidden"></div>
      <div class="title-band"><h1>Request for Study Participants</h1></div>
      <h2 class="headline">Efficiency of resources<br>available to survivors<br>of intimate partner abuse</h2>
      <ul class="questions">
        <li>Are you eighteen years of age or older?</li>
        <li>Have you been a victim of domestic violence?</li>
        <li>Have you sought assistance with abouse in the last 12 months?</li>
        <li>Are you still in contact with the person who abused you?</li>
        <li>Are you willing and open to discussing your experience with<br>abuse and your attempts to access services or resources?</li>
      </ul>
    </section>

    <section class="details">
      <p>If you answered yes to all of these questions, you may be eligible to participate in a study to better understand the resources needed and services expected for survivors of domestic violence.</p>
      <p>Please contact Dana Whitfield at <strong>1(555)014-2280</strong> or via e-mail<br><strong>survivorvoicesstudy@mailbox.example</strong> for additional information.</p>
      <p>Participants will be compensated for their time.</p>
      <p><strong>Principal Investigator:</strong> Dana Whitfield<br><strong>Institutional Affiliation:</strong> Lakeshore State University, Dept. of Criminology, Law and Justice</p>
      <p><strong>Contact Address:</strong> Post Office Box 100482, Rivermont, IL, 60000</p>
    </section>

    <div class="strip"></div>

    <section class="tear-offs">
      <div class="tab"><span>Survivor Research Study<br><b class="tab-phone">1(555)014-2280</b></span></div>
      <div class="tab"><span>Survivor Research Study<br><b class="tab-phone">1(555)014-2280</b></span></div>
      <div class="tab"><span>Survivor Research Study<br><b class="tab-phone">1(555)014-2280</b></span></div>
      <div class="tab"><span>Survivor Research Study<br><b class="tab-phone">1(555)014-2280</b></span></div>
      <div class="tab"><span>Survivor Research Study<br><b class="tab-phone">1(555)014-2280</b></span></div>
      <div class="tab"><span>Survivor Research Study<br><b class="tab-phone">1(555)014-2280</b></span></div>
      <div class="tab"><span>Survivor Research Study<br><b class="tab-phone">1(555)014-2280</b></span></div>
      <div class="tab"><span>Survivor Research Study<br><b class="tab-phone">1(555)014-2280</b></span></div>
      <div class="tab"><span>Survivor Research Study<br><b class="tab-phone">1(555)014-2280</b></span></div>
      <div class="tab"><span>Survivor Research Study<br><b class="tab-phone">1(555)014-2280</b></span></div>
      <div class="tab"><span>Survivor Research Study<br><b class="tab-phone">1(555)014-2280</b></span></div>
    </section>
  </main>
</body>
</html>
```